Quorvex - Automated robotic Inspection with AI need new business cards

We need a new design of our business cards. The company is focused on automated quality control at high speed with unmatched results. We have a logo but need a more forward leaning business card that shows that we are delivering cutting edge technology.

Contact Information for Business Card

Name
Position
Adress
Phone
Email
e.g.
Lena Holmqvist
Chief Financial Officer (CFO)

Quorvex Sweden AB
Bruksvägen 14, SE-175 43 JÄRFÄLLA, Sweden
Mobile: +46735 21 47 83 | Office: +46 8 61 94 27
www.quorvex-example.com

Font styles to use
Sans Serif

```html
<!DOCTYPE html>
<html lang="en">
<head>
<meta charset="UTF-8">
<title>Quorvex Business Cards</title>
<link rel="stylesheet" href="https://fonts.googleapis.com/css2?family=Montserrat:wght@400;500;600;700&display=swap">
<style>
  :root {
    --brand-blue: #1f5587;
    --ink-grey: #4a4f55;
    --card-white: #ffffff;
    --page-bg: #e4e6e9;
    --edge-blue: #9fc6e6;
  }
  * { box-sizing: border-box; margin: 0; padding: 0; }
  html, body { width: 1200px; height: 913px; overflow: hidden; }
  body {
    background: var(--page-bg);
    font-family: "Montserrat", sans-serif;
    position: relative;
  }
  .card {
    position: absolute;
    width: 640px;
    height: 366px;
    border-radius: 18px;
    box-shadow: 0 6px 18px rgba(0,0,0,0.18);
  }
  .card-back {
    left: 60px; top: 60px;
    background: var(--brand-blue);
    display: flex; align-items: center; justify-content: center;
  }
  .card-front {
    left: 500px; top: 487px;
    background: var(--card-white);
    box-shadow: 0 5px 0 var(--edge-blue), 0 10px 20px rgba(0,0,0,0.18);
  }
  .wordmark {
    display: flex; align-items: center; gap: 14px;
    font-weight: 700;
    letter-spacing: 2px;
  }
  .wordmark-dot {
    border-radius: 50%;
    flex: none;
  }
  .card-back .wordmark { color: var(--card-white); font-size: 64px; }
  .card-back .wordmark-dot { width: 46px; height: 46px; background: var(--card-white); }
  .card-front .wordmark {
    position: absolute; right: 70px; top: 62px;
    color: var(--brand-blue); font-size: 46px;
  }
  .card-front .wordmark-dot { width: 34px; height: 34px; background: var(--brand-blue); }
  .person {
    position: absolute; left: 44px; top: 196px;
  }
  .person-name {
    color: var(--brand-blue); font-weight: 700; font-size: 22px; letter-spacing: 1px;
  }
  .person-title {
    color: var(--ink-grey); font-size: 11.5px; letter-spacing: 0.6px; margin-top: 2px;
  }
  .contact-list {
    list-style: none; margin-top: 18px;
  }
  .contact-list li {
    display: flex; align-items: center; gap: 12px;
    color: var(--ink-grey); font-size: 14px; line-height: 23px;
  }
  .contact-list svg { width: 14px; height: 14px; fill: var(--brand-blue); flex: none; }
  .company {
    position: absolute; left: 376px; top: 206px;
    border-left: 2px solid var(--brand-blue);
    padding-left: 16px;
    font-size: 14px; line-height: 20px; color: var(--ink-grey);
  }
  .company-name { color: var(--brand-blue); font-weight: 600; }
</style>
</head>
<body>
  <section class="card card-back">
    <div class="wordmark"><span class="wordmark-dot"></span>QUORVEX</div>
  </section>

  <section class="card card-front">
    <div class="wordmark"><span class="wordmark-dot"></span>QUORVEX</div>

    <div class="person">
      <p class="person-name">LENA HOLMQVIST</p>
      <p class="person-title">CHIEF FINANCIAL OFFICER (CFO)</p>
      <ul class="contact-list">
        <li><svg viewBox="0 0 24 24" aria-hidden="true"><path d="M6.6 10.8a15 15 0 0 0 6.6 6.6l2.2-2.2a1 1 0 0 1 1-.25 11.4 11.4 0 0 0 3.6.6 1 1 0 0 1 1 1V20a1 1 0 0 1-1 1A17 17 0 0 1 3 4a1 1 0 0 1 1-1h3.5a1 1 0 0 1 1 1c0 1.25.2 2.45.6 3.6a1 1 0 0 1-.25 1z"/></svg>+46 8 61 94 27</li>
        <li><svg viewBox="0 0 24 24" aria-hidden="true"><path d="M7 1h10a2 2 0 0 1 2 2v18a2 2 0 0 1-2 2H7a2 2 0 0 1-2-2V3a2 2 0 0 1 2-2zm0 3v14h10V4zm5 15.5a1 1 0 1 0 0 2 1 1 0 0 0 0-2z"/></svg>+46735 21 47 83</li>
        <li><svg viewBox="0 0 24 24" aria-hidden="true"><path d="M2 5h20v14H2zm2 2v.5l8 5 8-5V7zm0 3v7h16v-7l-8 5z"/></svg>lena@quorvex-example.com</li>
        <li><svg viewBox="0 0 24 24" aria-hidden="true"><path d="M12 2a10 10 0 1 0 0 20 10 10 0 0 0 0-20zm-1 17.9A8 8 0 0 1 4.2 10L9 14.8V16a2 2 0 0 0 2 2zm6.9-2.5A2 2 0 0 0 16 16h-1v-3a1 1 0 0 0-1-1H8v-2h2a1 1 0 0 0 1-1V7h2a2 2 0 0 0 2-2v-.4a8 8 0 0 1 2.9 12.8z"/></svg>www.quorvex-example.com</li>
      </ul>
    </div>

    <address class="company" style="font-style:normal">
      <p class="company-name">Quorvex Sweden AB</p>
      <p>Bruksvägen 14, SE-175 43</p>
      <p>JÄRFÄLLA, Sweden</p>
    </address>
  </section>
</body>
</html>
```